Executive Business Card for Healthcare Company [Need Today]

I need a business card design for a healthcare company. The only branding the company has thus far is a logo. The cards will be utilized by company executives. The design I envision will be vibrant and appealing but with a corporate feel. They shouldn't be too casual or playful. I would like to complete this project TODAY if possible.

Target Market(s)

Healthcare vendors, other executives in healthcare and pharmaceuticals

Industry/Entity Type

Pharmaceutical

Contact Information for Business Card

See attachment

Font styles to use
Serif
Sans Serif

Colors

Designer to choose colors to be used in the design.

```html
<!DOCTYPE html>
<html lang="en">
<head>
<meta charset="utf-8">
<title>Calder Therapeutics – Business Card</title>
<link rel="stylesheet" href="https://fonts.googleapis.com/css2?family=Roboto:wght@300;400&display=swap">
<style>
  :root {
    --page-bg: #e9eaeb;
    --card-bg: #f7f8f8;
    --card-edge: #d9dcdc;
    --band-start: #15a0a6;
    --band-end: #3ca87c;
    --ring: #3aa27c;
    --brand-text: #6b6f72;
    --ink-light: #ffffff;
    --ink-soft: #e3f4f1;
    --ink-dark: #5c6064;
  }
  * { margin: 0; padding: 0; box-sizing: border-box; }
  html, body {
    width: 1200px;
    height: 1054px;
    overflow: hidden;
    background: var(--page-bg);
    font-family: "Roboto", Arial, sans-serif;
  }
  .business-card {
    position: absolute;
    left: 80px;
    top: 211px;
    width: 1040px;
    height: 632px;
    background: var(--card-bg);
    border: 1px solid var(--card-edge);
    border-radius: 4px;
    overflow: hidden;
  }
  .brand-name {
    position: absolute;
    left: 55px;
    top: 38px;
    color: var(--brand-text);
    font-weight: 300;
    line-height: 1;
  }
  .brand-name .brand-main {
    display: block;
    font-size: 84px;
    letter-spacing: 1px;
  }
  .brand-name .brand-sub {
    display: block;
    margin-left: 160px;
    margin-top: 6px;
    font-size: 44px;
  }
  .contact-band {
    position: absolute;
    left: 0;
    top: 242px;
    width: 100%;
    height: 293px;
    background: linear-gradient(90deg, var(--band-start) 0%, var(--band-end) 100%);
  }
  .emblem {
    position: absolute;
    left: 591px;
    top: 201px;
    width: 370px;
    height: 370px;
  }
  .holder-name {
    position: absolute;
    left: 55px;
    top: 302px;
    font-size: 42px;
    font-weight: 400;
    color: var(--ink-light);
  }
  .holder-title {
    position: absolute;
    left: 55px;
    top: 357px;
    font-size: 21px;
    font-weight: 400;
    color: var(--ink-soft);
  }
  .contact-list {
    position: absolute;
    left: 55px;
    top: 402px;
    list-style: none;
  }
  .contact-item {
    display: flex;
    align-items: center;
    height: 37px;
    font-size: 26px;
    font-weight: 300;
    color: var(--ink-light);
  }
  .contact-item svg {
    width: 24px;
    height: 24px;
    margin-right: 15px;
    fill: var(--ink-light);
  }
  .office-address {
    position: absolute;
    left: 55px;
    top: 567px;
    font-size: 25px;
    font-weight: 300;
    color: var(--ink-dark);
  }
</style>
</head>
<body>
  <main class="business-card">
    <div class="brand-name">
      <span class="brand-main">calder</span>
      <span class="brand-sub">therapeutics</span>
    </div>

    <div class="contact-band"></div>

    <svg class="emblem" viewBox="0 0 370 370" aria-hidden="true">
      <circle cx="185" cy="185" r="183" fill="var(--card-bg)"/>
      <circle cx="185" cy="185" r="166" fill="none" stroke="var(--ring)" stroke-width="9"/>
    </svg>

    <h1 class="holder-name">Daniel Hartley</h1>
    <p class="holder-title">Senior Director of Marketing</p>

    <ul class="contact-list">
      <li class="contact-item">
        <svg viewBox="0 0 24 24" aria-label="Office phone"><path d="M3 9c0-3 4-5 9-5s9 2 9 5v2h-5V9H8v2H3V9zm3 3h12l2 8H4l2-8zm6 1.5a2.5 2.5 0 1 0 0 5 2.5 2.5 0 0 0 0-5z"/></svg>
        555-214-7780
      </li>
      <li class="contact-item">
        <svg viewBox="0 0 24 24" aria-label="Mobile phone"><path d="M7 1h10a2 2 0 0 1 2 2v18a2 2 0 0 1-2 2H7a2 2 0 0 1-2-2V3a2 2 0 0 1 2-2zm0 3v14h10V4H7zm5 15.5a1.2 1.2 0 1 0 0 2.4 1.2 1.2 0 0 0 0-2.4z"/></svg>
        555-309-6612
      </li>
      <li class="contact-item">
        <svg viewBox="0 0 24 24" aria-label="Web"><path d="M12 2a10 10 0 1 0 0 20 10 10 0 0 0 0-20zm6.9 9h-3a15 15 0 0 0-1.4-6A8 8 0 0 1 18.9 11zM12 4.1c.9 1.3 1.7 3.8 1.9 6.9h-3.8c.2-3.1 1-5.6 1.9-6.9zM9.5 5a15 15 0 0 0-1.4 6h-3A8 8 0 0 1 9.5 5zm-4.4 8h3a15 15 0 0 0 1.4 6A8 8 0 0 1 5.1 13zm6.9 6.9c-.9-1.3-1.7-3.8-1.9-6.9h3.8c-.2 3.1-1 5.6-1.9 6.9zm2.5-.9a15 15 0 0 0 1.4-6h3a8 8 0 0 1-4.4 6z"/></svg>
        dhartley@calderrx.com
      </li>
    </ul>

    <p class="office-address">418 N Lumpkin Avenue Riverton, GA 30612</p>
  </main>
</body>
</html>
```